Steadfast MD - Sleep Medicine Specialist - Business Cards

We are a new medical practice called Steadfast MD. We are sleep medicine specialists and we will be conducting sleep studies on patients with sleep related ailments. We want the business card to be bold, professional, and clean with the logo as the stand out visual piece. We dont like wild flashy designs. We want our design to be bold and classic while at the same time conveying who we are and what we do. We are reliable, professional, and the best in the business.

Industry/Entity Type

Health Care

Contact Information for Business Card

- Clean
- Bold
- Classic
- not cluttered

Requirements
Must have
• logo, website, phone number
Nice to have
• several options to choose from
Should not have
• flashy imaged - reflective print - images of people sleeping

```html
<!DOCTYPE html>
<html lang="en">
<head>
<meta charset="utf-8">
<title>Steadfast MD – Business Card</title>
<link href="https://fonts.googleapis.com/css2?family=Lato:wght@400;700;900&display=swap" rel="stylesheet">
<style>
  :root {
    --page-bg: #e4e0da;
    --card-face: #f4f2ef;
    --band-black: #141414;
    --accent-red: #d0131c;
    --ink: #111111;
    --name-sand: #d8ccb9;
    --contact-light: #e9e6e1;
  }
  html, body {
    margin: 0;
    width: 1200px;
    height: 1047px;
    overflow: hidden;
    background: var(--page-bg);
    font-family: "Lato", sans-serif;
  }
  .card {
    position: absolute;
    left: 100px;
    top: 251px;
    width: 1000px;
    height: 545px;
    border-radius: 26px;
    background: var(--card-face);
    overflow: hidden;
    box-shadow: 0 10px 30px rgba(0,0,0,0.12);
  }
  .card-band {
    position: absolute;
    left: 0;
    right: 0;
    top: 306px;
    bottom: 0;
    background: var(--band-black);
    border-top: 11px solid var(--accent-red);
  }
  .brand {
    position: absolute;
    left: 201px;
    top: 49px;
    display: flex;
    align-items: center;
    gap: 24px;
  }
  .brand-mark {
    width: 120px;
    height: 120px;
    box-sizing: border-box;
    border: 7px solid var(--accent-red);
    border-radius: 50%;
  }
  .brand-name {
    font-weight: 900;
    font-size: 64px;
    letter-spacing: -1px;
    color: var(--ink);
    line-height: 1;
  }
  .holder {
    position: absolute;
    left: 40px;
    top: 398px;
    width: 330px;
    text-align: center;
  }
  .holder-name {
    font-weight: 700;
    font-size: 42px;
    letter-spacing: 1px;
    color: var(--name-sand);
    line-height: 1;
  }
  .holder-role {
    margin-top: 12px;
    font-size: 25px;
    color: var(--accent-red);
    line-height: 1;
  }
  .contact {
    position: absolute;
    left: 641px;
    top: 352px;
    color: var(--contact-light);
    font-size: 24px;
  }
  .address p { margin: 0; line-height: 30px; }
  .contact-list {
    list-style: none;
    margin: 10px 0 0;
    padding: 0;
  }
  .contact-list li {
    display: flex;
    align-items: center;
    height: 30px;
  }
  .contact-icon {
    width: 20px;
    height: 20px;
    margin: 0 23px 0 0;
    fill: var(--accent-red);
    flex: none;
  }
  .web-accent { color: var(--accent-red); }
</style>
</head>
<body>
  <div class="card">
    <div class="card-band"></div>

    <div class="brand">
      <div class="brand-mark"></div>
      <div class="brand-name">Steadfast MD</div>
    </div>

    <div class="holder">
      <div class="holder-name">DANIEL HART</div>
      <div class="holder-role">Founder &amp; CEO</div>
    </div>

    <div class="contact">
      <div class="address">
        <p>1234 First Line Address</p>
        <p>5678 Second Line Address</p>
      </div>
      <ul class="contact-list">
        <li>
          <svg class="contact-icon" viewBox="0 0 24 24"><path d="M6.6 10.8a15.1 15.1 0 0 0 6.6 6.6l2.2-2.2a1 1 0 0 1 1-.25 11.4 11.4 0 0 0 3.6.57 1 1 0 0 1 1 1V20a1 1 0 0 1-1 1A17 17 0 0 1 3 4a1 1 0 0 1 1-1h3.5a1 1 0 0 1 1 1c0 1.25.2 2.45.57 3.570a1 1 0 0 1-.25 1z"/></svg>
          <span>1234567890</span>
        </li>
        <li>
          <svg class="contact-icon" viewBox="0 0 24 24"><path d="M2 5h20v14H2z M3.5 6.5 12 13l8.5-6.5" stroke="var(--band-black)" stroke-width="1.5"/></svg>
          <span>info@yourmail.com</span>
        </li>
        <li>
          <svg class="contact-icon" viewBox="0 0 24 24"><g fill="none" stroke="var(--accent-red)" stroke-width="1.8"><circle cx="12" cy="12" r="9"/><ellipse cx="12" cy="12" rx="4" ry="9"/><path d="M3 12h18M5 7h14M5 17h14"/></g></svg>
          <span>www.<span class="web-accent">yourwebsite</span>.com</span>
        </li>
      </ul>
    </div>
  </div>
</body>
</html>
```